Stanbrook Fire Services Pty Ltd

We need business cards for a company based in Perth, we install, service and maintain fire equipment.
On the front we want a great design with our logo and a small spot for our full company name, general company email address and office number. On the back we need space for our name, title, mobile number and email address on the back.

Target Market(s)

Facility managers and commercial/industrial building owners/occupiers.

Contact Information for Business Card

Font styles to use
Sans Serif

Requirements
Must have
• Please only submit 5 of your best samples.
Darker tones are preferred.
Nice to have
• We want to use, black, red and grey. Keep it modern and clean.
I've attached the company logo and a sample of a boarder we use on our emergency plans.
Should not have
• No preference. Let the designer choose.

```html
<!DOCTYPE html>
<html lang="en">
<head>
<meta charset="UTF-8">
<title>Stanbrook Fire Services – Business Cards</title>
<link href="https://fonts.googleapis.com/css2?family=Poppins:wght@400;500;700&display=swap" rel="stylesheet">
<style>
  :root {
    --red: #e8222a;
    --black: #050505;
    --white: #ffffff;
    --stage: #2a2a2a;
  }
  * { margin: 0; padding: 0; box-sizing: border-box; }
  html, body { width: 1200px; height: 900px; overflow: hidden; }
  body {
    background: var(--stage);
    font-family: "Poppins", sans-serif;
    position: relative;
  }
  .card {
    position: absolute;
    left: 250px;
    width: 700px;
    height: 400px;
    overflow: hidden;
    box-shadow: 0 14px 30px rgba(0,0,0,.55);
  }
  .card--front { top: 35px; background: var(--white); }
  .card--back { top: 465px; background: var(--black); }

  .band {
    position: absolute;
    height: 40px;
    display: flex;
    align-items: center;
    gap: 12px;
    font-size: 17px;
    white-space: nowrap;
  }
  .band svg { width: 18px; height: 18px; flex: none; }

  /* front: bands run from left edge, slanted right end */
  .card--front .band { left: 0; padding-left: 60px; }
  .band--office {
    top: 140px; width: 400px; background: var(--black); color: var(--white);
    font-weight: 500; letter-spacing: 1px; padding-left: 120px !important;
    clip-path: polygon(0 0, 100% 0, calc(100% - 20px) 100%, 0 100%);
  }
  .band--office-phone {
    top: 186px; width: 380px; background: var(--red); color: var(--white);
    clip-path: polygon(0 0, 100% 0, calc(100% - 20px) 100%, 0 100%);
  }
  .band--office-mail {
    top: 232px; width: 360px; background: var(--red); color: var(--white);
    clip-path: polygon(0 0, 100% 0, calc(100% - 20px) 100%, 0 100%);
  }

  .brand {
    position: absolute;
    color: var(--red);
    font-weight: 700;
    letter-spacing: 1px;
    line-height: 1;
  }
  .card--front .brand { right: 36px; top: 200px; font-size: 36px; }
  .brand-legal {
    position: absolute;
    right: 36px; top: 250px;
    color: var(--red);
    font-size: 11px;
    font-weight: 500;
    letter-spacing: .6px;
    text-transform: uppercase;
  }

  /* back: bands run to right edge, slanted left end */
  .card--back .brand { left: 40px; top: 44px; font-size: 48px; }
  .card--back .band { right: 0; padding-left: 46px; }
  .band--name {
    top: 200px; width: 440px; background: var(--white); color: var(--black);
    clip-path: polygon(20px 0, 100% 0, 100% 100%, 0 100%);
  }
  .band--name .person { font-weight: 700; font-size: 19px; letter-spacing: .5px; }
  .band--name .role { color: var(--red); font-size: 12px; letter-spacing: .6px; align-self: flex-end; padding-bottom: 9px; }
  .band--mobile {
    top: 246px; width: 460px; background: var(--red); color: var(--white);
    clip-path: polygon(20px 0, 100% 0, 100% 100%, 0 100%);
  }
  .band--mail {
    top: 292px; width: 480px; background: var(--red); color: var(--white);
    clip-path: polygon(20px 0, 100% 0, 100% 100%, 0 100%);
  }
</style>
</head>
<body>

<section class="card card--front" aria-label="Business card front">
  <div class="band band--office">OFFICE</div>
  <div class="band band--office-phone">
    <svg viewBox="0 0 24 24" fill="currentColor" aria-hidden="true"><path d="M6.6 10.8a15.1 15.1 0 0 0 6.6 6.6l2.2-2.2a1 1 0 0 1 1-.25 11.4 11.4 0 0 0 3.6.57 1 1 0 0 1 1 1V20a1 1 0 0 1-1 1A17 17 0 0 1 3 4a1 1 0 0 1 1-1h3.5a1 1 0 0 1 1 1c0 1.25.2 2.450.57 3.57a1 1 0 0 1-.25 1z"/></svg>
    <span>0140 5582 7310</span>
  </div>
  <div class="band band--office-mail">
    <svg viewBox="0 0 24 24" fill="none" stroke="currentColor" stroke-width="2" aria-hidden="true"><rect x="2" y="5" width="20" height="14"/><path d="M2 5l10 8 10-8"/></svg>
    <span>info@stanbrookfire.com.au</span>
  </div>
  <div class="brand">STANBROOK</div>
  <div class="brand-legal">Stanbrook Fire Services Pty Ltd</div>
</section>

<section class="card card--back" aria-label="Business card back">
  <div class="brand">STANBROOK</div>
  <div class="band band--name">
    <span class="person">DANIEL HART</span>
    <span class="role">MANAGER</span>
  </div>
  <div class="band band--mobile">
    <svg viewBox="0 0 24 24" fill="none" stroke="currentColor" stroke-width="2" aria-hidden="true"><rect x="6" y="2" width="12" height="20" rx="2"/><path d="M11 18h2"/></svg>
    <span>0411-3287-5590</span>
  </div>
  <div class="band band--mail">
    <svg viewBox="0 0 24 24" fill="none" stroke="currentColor" stroke-width="2" aria-hidden="true"><rect x="2" y="5" width="20" height="14"/><path d="M2 5l10 8 10-8"/></svg>
    <span>daniel@stanbrookfire.com.au</span>
  </div>
</section>

</body>
</html>
```